Law Office needs stationery design and business card

I currently have been using the same letterhead for the last 8 years. Since i 'm about to adding another location, I want to revamp my letterhead and business card. I already have a logo i'm happy with. I will upload my current letterhead, fax sheet, envelope, and logos. I need a business card also. I have 2 locations, 1 phone number, 1 fax line, website, etc. If possible and fitting with the design, I would like to keep the same information listed currently on the letterhead.

**Keep in mind, I also NEED A FAX SHEET COVER. thank you
Updates

Hello, Please submit a Gray Scale or Black and White version of your designs also, since most of the time I will be printing NON color stationery. I will seldom use a color print for my letterhead, I would like to have a color version for my benefit, however i will print in grayscale majority of the time . For the Business Card, that can just be in color. When I get my business cards they will be in color.Thank youEnrique Added Sunday, September 18, 2016

Industry/Entity Type

Business

```html
<!DOCTYPE html>
<html lang="en">
<head>
<meta charset="utf-8">
<title>Halvern Law – Business Card</title>
<link href="https://fonts.googleapis.com/css2?family=Cinzel:wght@500;600&family=Roboto:wght@400;500&display=swap" rel="stylesheet">
<style>
  :root {
    --bg: #e2e2e2;
    --card: #ffffff;
    --ink: #211c1a;
    --gold: #c4a96a;
    --gold-text: #b89a55;
  }
  * { margin: 0; padding: 0; box-sizing: border-box; }
  html, body { width: 1200px; height: 900px; overflow: hidden; background: var(--bg); }
  .stage { position: relative; width: 1200px; height: 900px; }
  .card {
    position: absolute; width: 640px; height: 366px; background: var(--card);
    box-shadow: 0 2px 6px rgba(0,0,0,0.12); overflow: hidden;
  }
  .card-front { left: 100px; top: 70px; }
  .card-back { left: 460px; top: 470px; }

  .brand { display: flex; align-items: center; gap: 14px;
    font-family: "Cinzel", serif; font-weight: 600; color: var(--ink); letter-spacing: 0.04em; }
  .brand-mark { background: var(--ink); flex: none; }
  .card-front .brand { position: absolute; left: 0; right: 0; top: 150px; justify-content: center; font-size: 52px; }
  .card-front .brand-mark { width: 58px; height: 58px; }

  .card-back .wedges { position: absolute; left: 0; top: 0; }
  .card-back .brand { position: absolute; right: 38px; top: 48px; font-size: 26px; gap: 10px; }
  .card-back .brand-mark { width: 30px; height: 30px; }

  .person { position: absolute; left: 150px; top: 222px; font-family: "Cinzel", serif; }
  .person-name { font-size: 28px; font-weight: 500; color: var(--ink); line-height: 1; }
  .person-title { font-size: 11px; color: var(--gold-text); letter-spacing: 0.08em; margin-top: 4px; }
  .divider { position: absolute; left: 150px; right: 38px; top: 282px; height: 1px; background: var(--ink); }
  .contact { position: absolute; left: 150px; top: 292px; font-family: "Roboto", sans-serif;
    font-size: 10.5px; line-height: 17px; color: var(--ink); letter-spacing: 0.06em; }
  .contact .label { color: var(--gold-text); }
  .contact .web { font-weight: 500; }
</style>
</head>
<body>
<main class="stage">
  <section class="card card-front" aria-label="Business card front">
    <div class="brand"><span class="brand-mark"></span><span>Halvern Law</span></div>
  </section>

  <section class="card card-back" aria-label="Business card back">
    <svg class="wedges" width="640" height="366" viewBox="0 0 640 366" aria-hidden="true">
      <path d="M0,0 L262,0 Q100,80 0,140 Z" fill="var(--ink)"/>
      <path d="M0,140 Q100,80 262,0 L300,0 Q120,95 0,205 Z" fill="var(--gold)"/>
    </svg>
    <div class="brand"><span class="brand-mark"></span><span>Halvern Law</span></div>
    <div class="person">
      <p class="person-name">Enrique Tobias</p>
      <p class="person-title">MANAGER</p>
    </div>
    <div class="divider"></div>
    <div class="contact">
      <p>48 Orchard Lane, Suite 210, Ashford, PA 19071 | 917 Linden Ave, Carrow, PA 19045</p>
      <p><span class="label">phone</span> 610 555 0182 | <span class="label">fax</span> 484 555 0147 | Enrique@HalvernLaw.com</p>
      <p class="web">www.HalvernLaw.com</p>
    </div>
  </section>
</main>
</body>
</html>
```